Norvane Builders Business Card

Modern and Professional Business Card for a Med size construction/development company.

See the samples below for the design I like … but I need ideas for incorporating the red company logo while still keeping the clean look of the card samples that are attached.

Logo and tag line on the back … info on the front.

Tagline: Quality Starts from the Ground Up

Target Market(s)

Med-Large General Contractors

Contact Information for Business Card

Norvane Builders Limited
42 Brenton Street
Elk Harbour, NL
B3K 7T2

t: 709-555-0147
f: 709-555-0192
w: www.norvanebuilders-example.com

Font styles to use
Sans Serif

Colors
fbee3e

Requirements
Must have
• I like the black and yellow designs of the attached samples …. but I'm not sure how to incorporate the red Norvane Builders logo into that design??
Nice to have
• Construction safety strips

```html
<!DOCTYPE html>
<html lang="en">
<head>
<meta charset="utf-8">
<title>Norvane Builders Business Card</title>
<link rel="stylesheet" href="https://fonts.googleapis.com/css2?family=Open+Sans:wght@300;400;600;700&display=swap">
<style>
  :root {
    --page: #ffffff;
    --front-light: #f4f4f4;
    --front-mid: #e4e4e4;
    --back-dark: #3f4447;
    --back-mid: #5a5f62;
    --ink: #1f1f1f;
    --ink-soft: #555555;
    --brand-red: #e2343a;
    --safety-yellow: #fbee3e;
    --white: #ffffff;
  }
  * { box-sizing: border-box; margin: 0; padding: 0; }
  html, body {
    width: 941px; height: 1200px; overflow: hidden;
    background: var(--page);
    font-family: "Open Sans", Arial, sans-serif;
  }
  .sheet { position: relative; width: 941px; height: 1200px; }

  .card {
    position: absolute; left: 140px; width: 700px; height: 412px; overflow: hidden;
  }
  .card-front { top: 162px; }
  .card-back { top: 681px; }

  .backdrop { position: absolute; inset: 0; }
  .card-front .backdrop {
    background: linear-gradient(120deg, var(--front-mid) 0%, var(--front-light) 45%, var(--white) 75%, var(--front-mid) 100%);
  }
  .card-back .backdrop {
    background: linear-gradient(120deg, var(--back-dark) 0%, var(--back-mid) 50%, var(--back-dark) 100%);
  }

  .identity {
    position: absolute; right: 389px; top: 138px; text-align: right;
  }
  .company-name {
    font-weight: 700; font-size: 30px; line-height: 1.1; color: var(--ink); white-space: nowrap;
  }
  .company-suffix {
    margin-top: 12px; font-size: 14px; letter-spacing: 1px; color: var(--ink-soft);
  }

  .contact {
    position: absolute; left: 344px; top: 144px;
    list-style: none;
    font-weight: 700; font-size: 15px; line-height: 26px; color: var(--ink);
  }
  .contact li { white-space: nowrap; }

  .brand-block {
    position: absolute; left: 151px; top: 68px; width: 392px; height: 197px;
    display: flex; align-items: center; justify-content: center; gap: 14px;
  }
  .brand-square { width: 28px; height: 28px; background: var(--brand-red); flex: none; }
  .brand-name {
    font-weight: 700; font-size: 28px; color: var(--white); white-space: nowrap;
  }

  .tagline {
    position: absolute; left: 0; right: 0; top: 287px; text-align: center;
    font-weight: 400; font-size: 16px; letter-spacing: 5px;
    text-transform: uppercase; color: var(--safety-yellow);
  }
</style>
</head>
<body>
<main class="sheet">
  <section class="card card-front">
    <div class="backdrop" role="img" aria-label="Faint photograph of a steel roof frame structure"></div>
    <div class="identity">
      <h1 class="company-name">Norvane Builders</h1>
      <p class="company-suffix">LIMITED</p>
    </div>
    <ul class="contact">
      <li>Mobile: (709) 555 0147</li>
      <li>Fax: (709) 555 0192</li>
      <li>Address: 42 Brenton Street, Elk Harbour,</li>
      <li>NL B3K 7T2</li>
      <li>Website: www.norvanebuilders-example.com</li>
    </ul>
  </section>

  <section class="card card-back">
    <div class="backdrop" role="img" aria-label="Dark photograph of a steel roof frame structure"></div>
    <div class="brand-block">
      <span class="brand-square"></span>
      <span class="brand-name">Norvane Builders Limited</span>
    </div>
    <p class="tagline">Quality starts from the ground up</p>
  </section>
</main>
</body>
</html>
```